Vantorique Business Card and Letter Head

We are a leadership assessment consultancy based in Sydney, Australia. We help executive-level decison-makers select leaders for more senior level roles in corporate and government organisations. Our methodology is based on the latest research from the field of neuroscience.
We need a business card design and matching letter head that presents our company, Vantorique, as a:
1. trusted adviser to senior executive-level decison makers
2. niche consultancy who are experts in the field of assessing leadership talent
3. results-focused solution provider who balance scientific methods with pragmatic solutions
The following company details should be used in all designs:
Company Name: Vantorique
Details (for business card):
Daniel Prewett
Leadership Talent Officer
Level 17, Marrowby Tower
14 Tallowin Square
Sydney, NSW 2000 Australia
Phone: 1300 582 714
Mobile: 0412 637 208
Email: daniel.prewett@vantorique.com.au
Website: vantorique.com.au
I have attached the logo for Vantorique (for both a white and black background) - your business card and letter head designs must incoporate this logo and colour scheme.
Thanks for your interest in this project, I'm looking forward to receiving your ideas.
Regards,
Daniel
Target Market(s)
Executive-level decison-makers in corporate and government organisations (e.g., CEO, VP, Head of Human Resources)
Industry/Entity Type
Leadership
Look and feel
Each slider illustrates characteristics of the customer's brand and the style your logo design should communicate.

```html
<!DOCTYPE html>
<html lang="en">
<head>
<meta charset="utf-8">
<title>Vantorique Stationery</title>
<link href="https://fonts.googleapis.com/css2?family=Arimo:wght@400;700&family=Roboto+Condensed:wght@400&family=Quicksand:wght@400&display=swap" rel="stylesheet">
<style>
:root{
  --bg:#ece6de;
  --paper:#ffffff;
  --charcoal:#434345;
  --mid-grey:#9b9b9d;
  --ink:#3a3a3c;
  --accent:#c8391f;
  --soft-line:#dcdcdc;
}
*{margin:0;padding:0;box-sizing:border-box}
html,body{width:1200px;height:834px;overflow:hidden;background:var(--bg)}
.canvas{position:relative;width:1200px;height:834px}
.piece{position:absolute;background:var(--paper)}
.dark-panel{background:radial-gradient(ellipse at center,var(--mid-grey) 0%,#6a6a6c 45%,var(--charcoal) 80%)}
.accent-rule{position:absolute;left:0;right:0;height:3px;background:linear-gradient(90deg,rgba(200,57,31,0),var(--accent) 50%,rgba(200,57,31,0))}
.soft-rule{position:absolute;height:6px;background:linear-gradient(90deg,rgba(0,0,0,0),var(--soft-line) 50%,rgba(0,0,0,0))}
.wordmark{display:flex;align-items:center;gap:8px;font-family:"Arimo",sans-serif;font-weight:700;color:var(--ink);white-space:nowrap}
.wordmark .mark-square{display:inline-block;background:var(--ink)}
.wordmark.on-dark{color:#f2f2f2}
.wordmark.on-dark .mark-square{background:#f2f2f2}
.address{font-family:"Roboto Condensed",sans-serif;font-size:8px;line-height:11px;color:#222}
.web{position:absolute;left:0;right:0;text-align:center;font-family:"Quicksand",sans-serif;color:var(--accent);letter-spacing:.5px}
.title-line{font-family:"Quicksand",sans-serif;color:var(--accent)}

/* letterhead */
.letterhead{left:26px;top:39px;width:533px;height:753px}
.letterhead .top-band{position:absolute;left:0;right:0;top:0;height:26px;background:linear-gradient(90deg,var(--charcoal),#8f8f91 50%,var(--charcoal))}
.letterhead .accent-rule{top:26px}
.letterhead .wordmark{position:absolute;left:111px;top:45px;font-size:19px}
.letterhead .mark-square{width:14px;height:14px}
.divider{position:absolute;width:1px;background:#999}
.letterhead .divider{left:275px;top:42px;height:38px}
.letterhead .address{position:absolute;left:296px;top:44px}
.letterhead .soft-rule{left:10px;right:10px;top:718px}
.letterhead .web{top:734px;font-size:12px}

/* business cards */
.card-back{left:106px;top:224px;width:293px;height:163px}
.card-back .centre{position:absolute;inset:0;display:flex;align-items:center;justify-content:center}
.card-back .mark-square{width:40px;height:40px;background:rgba(255,255,255,.25)}
.card-front{left:201px;top:418px;width:296px;height:164px}
.card-front .dark-panel{position:absolute;left:0;right:0;top:0;height:82px}
.card-front .accent-rule{top:82px}
.card-front .identity{position:absolute;left:58px;top:23px;display:flex;gap:8px}
.card-front .mark-square{width:16px;height:16px;background:#f2f2f2;margin-top:3px}
.card-front .name{font-family:"Arimo",sans-serif;font-weight:700;font-size:18px;color:#f2f2f2;line-height:20px}
.card-front .role{font-family:"Arimo",sans-serif;font-size:12px;color:#d4d4d4;line-height:16px}
.contact-col{position:absolute;top:95px;font-family:"Arimo",sans-serif;font-size:7px;line-height:11px;color:#333}
.contact-col.left{left:45px}
.contact-col.right{left:166px;text-align:right;width:90px}
.contact-col .icon{display:inline-block;width:5px;height:6px;margin-right:6px;background:#bbb;vertical-align:middle}
.card-front .soft-rule{left:0;right:0;top:137px}
.card-front .web{top:146px;font-size:10px}

/* envelope */
.envelope-flap{position:absolute;left:579px;top:58px}
.envelope{left:579px;top:172px;width:598px;height:261px}
.envelope .accent-rule{top:0}
.envelope .wordmark{position:absolute;left:25px;top:40px;font-size:17px}
.envelope .mark-square{width:12px;height:12px}
.envelope .divider{left:170px;top:36px;height:36px}
.envelope .address{position:absolute;left:185px;top:38px;font-size:7px;line-height:10px}
.envelope .soft-rule{left:10px;right:10px;top:233px}
.envelope .web{top:244px;font-size:10px}

/* disc and sleeve */
.disc{position:absolute;left:843px;top:471px}
.sleeve{left:602px;top:473px;width:306px;height:317px}
.sleeve .dark-panel{position:absolute;left:0;right:0;top:0;height:160px}
.sleeve .accent-rule{top:160px}
.sleeve .wordmark{position:absolute;left:0;right:0;top:63px;justify-content:center;font-size:26px}
.sleeve .mark-square{width:20px;height:20px}
.sleeve .title-line{position:absolute;left:0;right:0;top:183px;text-align:center;font-size:18px}
.sleeve .soft-rule{left:0;right:0;top:293px}
.sleeve .web{top:300px;font-size:11px;color:#333}
</style>
</head>
<body>
<div class="canvas">

  <section class="piece letterhead">
    <div class="top-band"></div>
    <div class="accent-rule"></div>
    <div class="wordmark"><span class="mark-square"></span>Vantorique</div>
    <div class="divider"></div>
    <p class="address">Level 17, Marrowby Tower, 14 Tallowin Square,<br>Sydney NSW 2000 Australia<br>Phone: 1300 582 714 &nbsp; Mobile: 0412 637 208</p>
    <div class="soft-rule"></div>
    <p class="web">www.vantorique.com.au</p>
  </section>

  <section class="piece card-back dark-panel">
    <div class="centre"><span class="wordmark on-dark" style="font-size:22px"><span class="mark-square"></span>Vantorique</span></div>
  </section>

  <section class="piece card-front">
    <div class="dark-panel"></div>
    <div class="accent-rule"></div>
    <div class="identity">
      <span class="mark-square"></span>
      <div><p class="name">Daniel Prewett</p><p class="role">Leadership Talent Officer</p></div>
    </div>
    <p class="contact-col left"><span class="icon"></span>Phone: 1300 582 714<br><span class="icon"></span>Mobile: 0412 637 208<br><span class="icon"></span>daniel.prewett@vantorique.com.au</p>
    <p class="contact-col right">Level 17, Marrowby Tower<br>14 Tallowin Square &nbsp;Sydney<br>NSW 2000 Australia</p>
    <div class="soft-rule"></div>
    <p class="web">www.vantorique.com.au</p>
  </section>

  <svg class="envelope-flap" width="598" height="116" viewBox="0 0 598 116">
    <defs>
      <linearGradient id="flapShade" x1="0" x2="1">
        <stop offset="0" stop-color="#434345"/><stop offset=".5" stop-color="#a3a3a5"/><stop offset="1" stop-color="#434345"/>
      </linearGradient>
    </defs>
    <path d="M0 114 L35 70 Q60 44 130 36 Q300 0 468 36 Q538 44 563 70 L598 114 Z" fill="url(#flapShade)"/>
    <rect x="285" y="40" width="28" height="28" fill="#ffffff" fill-opacity=".25"/>
  </svg>
  <section class="piece envelope">
    <div class="accent-rule"></div>
    <div class="wordmark"><span class="mark-square"></span>Vantorique</div>
    <div class="divider"></div>
    <p class="address">Level 17, Marrowby Tower, 14 Tallowin Square,<br>Sydney NSW 2000 Australia<br>Phone: 1300 582 714 &nbsp; Mobile: 0412 637 208</p>
    <div class="soft-rule"></div>
    <p class="web">www.vantorique.com.au</p>
  </section>

  <svg class="disc" width="324" height="324" viewBox="0 0 324 324">
    <defs>
      <clipPath id="discClip"><circle cx="162" cy="162" r="160"/></clipPath>
      <radialGradient id="discShade" cx=".5" cy=".35" r=".6">
        <stop offset="0" stop-color="#a0a0a2"/><stop offset="1" stop-color="#444446"/>
      </radialGradient>
      <mask id="discHole"><rect width="324" height="324" fill="#fff"/><circle cx="162" cy="162" r="33" fill="#000"/></mask>
    </defs>
    <g mask="url(#discHole)">
      <circle cx="162" cy="162" r="161" fill="#ffffff" stroke="#cfcfcf" stroke-width="2"/>
      <g clip-path="url(#discClip)">
        <polygon points="0,0 324,0 324,198 0,121" fill="url(#discShade)"/>
        <line x1="0" y1="122" x2="324" y2="199" stroke="#c8391f" stroke-width="3"/>
      </g>
      <circle cx="162" cy="162" r="148" fill="none" stroke="#ffffff" stroke-opacity=".7"/>
      <rect x="210" y="86" width="34" height="34" fill="#ffffff" fill-opacity=".22"/>
    </g>
    <text x="84" y="224" transform="rotate(22 84 224)" font-family="Quicksand, sans-serif" font-size="22" fill="#c8391f">Your Title Here</text>
    <text x="72" y="282" transform="rotate(22 72 282)" font-family="Quicksand, sans-serif" font-size="11" fill="#333">www.vantorique.com.au</text>
  </svg>

  <section class="piece sleeve">
    <div class="dark-panel"></div>
    <div class="accent-rule"></div>
    <div class="wordmark on-dark"><span class="mark-square"></span>Vantorique</div>
    <p class="title-line">Your Title Here</p>
    <div class="soft-rule"></div>
    <p class="web">www.vantorique.com.au</p>
  </section>

</div>
</body>
</html>
```